need a business card designed, I work with independent car dealerships throughout the US, I connect them with Buyers ( private investors, banks, credit unions, finance co's etc... ) that want to purchase their loan portfolio's, also consult on cashflow management, business lines of credit etc... looking for a consultant look, but something that attracts small business owners
Dunmore Consulting

```html
<!DOCTYPE html>
<html lang="en">
<head>
<meta charset="utf-8">
<title>Dunmore Consulting – Business Card</title>
<link rel="stylesheet" href="https://fonts.googleapis.com/css2?family=Cabin:wght@400;500;600&display=swap">
<style>
  :root {
    --page-bg: #ffffff;
    --card-border: #8a8a8a;
    --ink-dark: #0c1416;
    --ink-body: #222a2c;
    --brand-slate: #2f434b;
    --brand-silver: #c9cccd;
    --divider: #cfcfcf;
    --white: #ffffff;
  }
  * { margin: 0; padding: 0; box-sizing: border-box; }
  html, body {
    width: 1200px;
    height: 1000px;
    overflow: hidden;
    background: var(--page-bg);
    font-family: "Cabin", Arial, sans-serif;
  }
  .sheet { position: relative; width: 1200px; height: 1000px; }

  .card { position: absolute; left: 196px; width: 809px; }

  /* Front */
  .card-front {
    top: 22px;
    height: 464px;
    background: var(--white);
    border: 1px solid var(--card-border);
  }
  .brand-front {
    position: absolute;
    top: 150px;
    left: 0;
    width: 100%;
    display: flex;
    justify-content: center;
    align-items: center;
    gap: 14px;
    color: var(--brand-slate);
    font-size: 42px;
    font-weight: 600;
    letter-spacing: 0.5px;
  }
  .brand-mark {
    width: 18px;
    height: 18px;
    background: var(--brand-slate);
  }
  .name-band {
    position: absolute;
    top: 304px;
    left: -1px;
    width: 809px;
    height: 50px;
    background: var(--ink-dark);
    color: var(--white);
    font-size: 26px;
    line-height: 50px;
    text-align: center;
  }
  .contact {
    position: absolute;
    top: 366px;
    left: 0;
    width: 100%;
    text-align: center;
    color: var(--ink-body);
    font-size: 22px;
    line-height: 31px;
  }

  .page-divider {
    position: absolute;
    top: 497px;
    left: 0;
    width: 1200px;
    height: 2px;
    background: var(--divider);
  }

  /* Back */
  .card-back {
    top: 514px;
    height: 462px;
    background: var(--ink-dark);
  }
  .brand-back {
    position: absolute;
    top: 210px;
    left: 0;
    width: 100%;
    display: flex;
    justify-content: center;
    align-items: center;
    gap: 14px;
    color: var(--brand-silver);
    font-size: 44px;
    font-weight: 600;
    letter-spacing: 0.5px;
  }
  .brand-back .brand-mark { background: var(--brand-silver); }
  .back-rule {
    position: absolute;
    top: 307px;
    left: 251px;
    width: 306px;
    height: 1px;
    background: #8f9496;
  }
  .website {
    position: absolute;
    top: 310px;
    left: 0;
    width: 100%;
    text-align: center;
    color: var(--white);
    font-size: 22px;
    line-height: 30px;
  }
</style>
</head>
<body>
  <main class="sheet">
    <section class="card card-front" aria-label="Card front">
      <div class="brand-front">
        <span class="brand-mark" aria-hidden="true"></span>
        <span class="brand-name">Dunmore Consulting</span>
      </div>
      <div class="name-band">Nathan DUNMORE | Consultant</div>
      <div class="contact">
        <p>Phone: 000.000.0000 | Fax: 000.000.0000</p>
        <p>Email: office@dunmoreconsulting.com</p>
      </div>
    </section>

    <div class="page-divider"></div>

    <section class="card card-back" aria-label="Card back">
      <div class="brand-back">
        <span class="brand-mark" aria-hidden="true"></span>
        <span class="brand-name">Dunmore Consulting</span>
      </div>
      <div class="back-rule"></div>
      <p class="website">www.dunmoreconsulting.com</p>
    </section>
  </main>
</body>
</html>
```